Shopping centre customer engagement software website

We need a multi page site with :

*What we do.
*How it works.
*Benefits
* Case study
* Testimonial
* Business login (we provide link to business portal)
* Consumer login (we provide link to consumer site)
* Book a demo
* Contact us

We want it to be clean and crisp and very self explanatory with little clutter. We are thinking white but are open to what ever looks the best.
Updates

Wordpress is preferred

Need extra days to review

Target Market(s)

Shopping centre managers and retail property companies

Coding

Coded - Design and coding required

Number of Pages Required

5+ page

Font styles to use
Sans Serif

Colors
ffffff

Requirements
Must have
• As listed above and must be responsive! Checkout our existing site for the text to be included (will be edited but it’ll give you an idea) www.vantrizo.com

```html
<!DOCTYPE html>
<html lang="en">
<head>
<meta charset="utf-8">
<title>Vantrizo – A Web App That Puts You On Top</title>
<link rel="stylesheet" href="https://fonts.googleapis.com/css2?family=Raleway:wght@400;600;700&family=Open+Sans:wght@400;600&display=swap">
<style>
:root{
  --navy:#2b2f3e;
  --navy-deep:#232634;
  --slate:#464b5a;
  --pink:#ef2f74;
  --pink-soft:#f7729a;
  --peach:#f9a98f;
  --ink:#2c2f36;
  --text:#5d6069;
  --muted:#8b8e96;
  --mist:#f5f6fa;
  --line:#e3e5ea;
  --white:#ffffff;
  --map:#e9eaec;
}
*{margin:0;padding:0;box-sizing:border-box}
html,body{width:1200px;height:4138px;overflow:hidden}
body{position:relative;background:var(--white);font-family:'Open Sans',Arial,sans-serif;color:var(--text)}
.abs{position:absolute}
h1,h2,h3,h4{font-family:'Raleway',Arial,sans-serif}

/* hero */
.hero{left:0;top:0;width:1200px;height:629px;background:radial-gradient(ellipse at 50% 70%,#353a4c 0%,var(--navy) 55%,var(--navy-deep) 100%)}
.nav{top:34px;right:0;width:1200px;height:24px}
.nav a{position:absolute;top:0;color:var(--white);font-size:14px;text-decoration:none;white-space:nowrap}
.hero-title{left:0;width:1200px;top:224px;text-align:center;color:var(--white);font-size:33px;font-weight:700;letter-spacing:.5px}
.hero-sub{left:0;width:1200px;top:290px;text-align:center;color:var(--white);font-family:'Open Sans',Arial,sans-serif;font-size:24px;line-height:38px}
.device{border-radius:14px}
.hero-laptop{left:250px;top:455px;width:676px;height:395px;background:linear-gradient(180deg,#1d1f26 0%,#30333d 78%,#c9ccd2 80%,#eceef1 100%)}

/* features */
.feature{top:960px;width:220px;text-align:center}
.feature svg{display:block;margin:0 auto 22px}
.feature h4{font-size:12px;font-weight:700;color:var(--ink);letter-spacing:.3px;margin-bottom:10px}
.feature p{font-size:11px;line-height:16px;color:var(--muted)}

/* section heads */
.section-head{left:0;width:1200px;text-align:center}
.section-head h2{font-size:21px;font-weight:600;color:var(--ink);letter-spacing:.5px}
.divider{margin:14px auto 16px;width:90px;height:10px;position:relative}
.divider:before,.divider:after{content:"";position:absolute;top:5px;width:36px;height:1px;background:var(--pink-soft)}
.divider:before{left:0}.divider:after{right:0}
.divider span{position:absolute;left:41px;top:1px;width:8px;height:8px;border:1px solid var(--pink-soft);border-radius:50%}
.section-head p{font-size:11px;line-height:17px;color:var(--text)}

/* about */
.about{left:0;top:1236px;width:1200px;height:723px;background:var(--mist)}
.about-copy{left:166px;top:1555px;width:460px}
.about-copy h3{font-size:17px;font-weight:600;color:var(--ink);margin-bottom:18px}
.about-copy p{font-size:14px;line-height:22.5px;color:var(--text)}
.about-laptop{left:635px;top:1559px;width:386px;height:248px;background:linear-gradient(180deg,#2a2c33 0%,#f3f4f6 6%,#ffffff 50%,#f3f4f6 88%,#d4d7dc 92%,#eef0f3 100%)}

/* faq */
.timeline{left:138px;top:2175px;width:2px;height:350px;background:var(--line)}
.faq-item{left:170px;width:423px;background:var(--white);box-shadow:0 2px 8px rgba(40,44,60,.12);border-left:3px solid var(--line)}
.faq-item.open{border-left-color:var(--pink)}
.faq-item h4{font-family:'Raleway',Arial,sans-serif;font-size:13px;font-weight:600;color:var(--ink);padding:0 50px 0 14px;line-height:44px}
.faq-item p{font-size:11px;line-height:16px;color:var(--text);padding:0 40px 14px 14px}
.faq-item .toggle{position:absolute;right:14px;top:15px;width:14px;height:14px;border:1.5px solid var(--pink);border-radius:50%}
.faq-item .toggle:after{content:"";position:absolute;left:3px;top:3px;border-left:5px solid var(--pink);border-top:2.5px solid transparent;border-bottom:2.5px solid transparent}
.faq-item.open .toggle:after{left:2px;top:4px;border-top:5px solid var(--pink);border-left:2.5px solid transparent;border-right:2.5px solid transparent;border-bottom:0}
.node{left:131px;width:16px;height:16px;border-radius:50%;background:var(--white);border:2px solid #c8cbd2}
.faq-phone{left:662px;top:2166px;width:337px;height:367px;border-radius:40px;background:linear-gradient(160deg,#f5f2ef 0%,#ffffff 30%,#fde3ea 55%,#f3f4f6 100%)}

/* cta */
.cta{left:0;top:2629px;width:1200px;height:392px;background:linear-gradient(90deg,var(--pink) 0%,#f36286 55%,var(--peach) 100%)}
.cta h2{left:171px;top:2732px;color:var(--white);font-size:25px;font-weight:700;letter-spacing:.5px}
.cta-text{left:171px;top:2777px;width:480px;color:var(--white);font-size:11px;line-height:16px}
.btn-ghost{left:240px;top:2853px;width:135px;height:33px;border:2px solid var(--white);border-radius:18px;color:var(--white);font-family:'Raleway',Arial,sans-serif;font-weight:700;font-size:13px;text-align:center;line-height:29px;letter-spacing:.5px}
.cta-phones{left:841px;top:2731px;width:359px;height:290px;border-radius:30px 0 0 0;background:linear-gradient(160deg,#4a4d57 0%,#ffffff 35%,#fbc6d4 60%,#f2f3f5 100%)}

/* map + subscribe */
.map{left:0;top:3200px;width:1200px;height:552px;background:linear-gradient(135deg,#eeeff1 0%,var(--map) 50%,#e1e3e6 100%)}
.map-pin{left:580px;top:3446px;width:26px;height:26px;border-radius:50%;background:#6fc4ef;box-shadow:0 0 0 10px rgba(111,196,239,.3)}
.subscribe{left:160px;top:3145px;width:877px;height:111px;background:var(--navy)}
.subscribe h3{position:absolute;left:108px;top:42px;color:var(--white);font-size:18px;font-weight:700;letter-spacing:.3px}
.subscribe .field{position:absolute;left:340px;top:30px;width:490px;height:50px;background:var(--white);border-radius:25px;font-size:13px;color:var(--ink);line-height:50px;padding-left:40px}
.subscribe .send{position:absolute;right:0;top:0;width:120px;height:50px;border-radius:25px;background:linear-gradient(90deg,var(--pink),#f6728f);display:flex;align-items:center;justify-content:center}

/* footer */
.footer{left:0;top:3752px;width:1200px;height:386px;background:var(--navy)}
.contact-card{left:160px;top:3485px;width:516px;height:507px;background:var(--white)}
.contact-card h3{position:absolute;left:77px;top:88px;font-size:20px;font-weight:600;color:var(--ink)}
.input{position:absolute;left:77px;width:358px;border-bottom:1px solid #c6c8ce;font-size:11px;color:var(--ink);padding-bottom:8px}
.btn-send{position:absolute;left:77px;top:437px;width:130px;height:28px;border-radius:14px;background:linear-gradient(90deg,var(--pink),#f6728f);color:var(--white);font-family:'Raleway',Arial,sans-serif;font-size:9px;font-weight:700;letter-spacing:1px;text-align:center;line-height:28px}
.address-panel{left:676px;top:3485px;width:386px;height:507px;background:var(--slate)}
.address-panel h3{position:absolute;left:68px;top:88px;font-size:20px;font-weight:600;color:var(--white)}
.address-panel p.lead{position:absolute;left:68px;top:138px;width:290px;color:var(--white);font-size:13px;line-height:20px}
.contact-line{position:absolute;left:68px;display:flex;align-items:flex-start;gap:14px;color:var(--white);font-size:13px;line-height:18px}
.contact-line .ico{width:22px;height:22px;border:1.5px solid var(--white);border-radius:50%;display:flex;align-items:center;justify-content:center;flex:none}
.socials{left:0;width:1200px;top:4044px;display:flex;justify-content:center;gap:11px}
.socials span{width:24px;height:24px;border-radius:50%;background:var(--white)}
.copyright{left:0;width:1200px;top:4089px;text-align:center;color:#c4c6cd;font-size:11px}
</style>
</head>
<body>

<section class="abs hero" aria-label="Hero"></section>
<nav class="abs nav">
  <a style="left:293px">What we do</a>
  <a style="left:413px">How it works</a>
  <a style="left:548px">Benefits</a>
  <a style="left:630px">Case study</a>
  <a style="left:741px">Testimonial</a>
  <a style="left:859px">Login</a>
  <a style="left:930px">Book a demo</a>
  <a style="left:1059px">Contact us</a>
</nav>
<h1 class="abs hero-title">A WEB APP THAT PUTS YOU ON TOP</h1>
<p class="abs hero-sub">Delight Your Shoppers, Impress Your Tenants And Provide<br>Your Landlords With Accurate &amp; Detailed Data In Real Time</p>
<div class="abs device hero-laptop" role="img" aria-label="Laptop showing the web app dashboard"></div>

<div class="abs feature" style="left:158px">
  <svg width="36" height="36" viewBox="0 0 36 36" fill="none" stroke-width="2"><path d="M18 4v20" stroke="#f2a12c"/><path d="M10 24h16l-3 8H13z" stroke="#3f8fd8"/><circle cx="18" cy="8" r="3" stroke="#ef2f74"/></svg>
  <h4>EASY TO USE</h4>
  <p>A simple layout lets every shopper find offers fast with no steps to learn.</p>
</div>
<div class="abs feature" style="left:376px">
  <svg width="36" height="36" viewBox="0 0 36 36" fill="none" stroke-width="2"><rect x="6" y="6" width="24" height="24" stroke="#3f8fd8"/><path d="M10 26l16-16" stroke="#ef2f74"/><path d="M10 14h8" stroke="#f2a12c"/></svg>
  <h4>AWESOME DESIGN</h4>
  <p>Clean screens keep your centre brand in front of shoppers at every visit.</p>
</div>
<div class="abs feature" style="left:599px">
  <svg width="36" height="36" viewBox="0 0 36 36" fill="none" stroke-width="2"><path d="M8 28L26 10" stroke="#f2a12c"/><path d="M8 10l18 18" stroke="#3f8fd8"/><circle cx="27" cy="9" r="3" stroke="#ef2f74"/></svg>
  <h4>EASY TO CUSTOMIZE</h4>
  <p>Change colours, offers and alerts for each tenant in just a few clicks.</p>
</div>
<div class="abs feature" style="left:820px">
  <svg width="36" height="36" viewBox="0 0 36 36" fill="none" stroke="#2c2f36" stroke-width="2"><path d="M8 20v-4a10 10 0 0 1 20 0v4"/><rect x="6" y="19" width="5" height="9" rx="2"/><rect x="25" y="19" width="5" height="9" rx="2"/></svg>
  <h4>24/7 ONLINE SUPPORT</h4>
  <p>Our team is on hand day and night to answer any question you may have.</p>
</div>

<section class="abs about" aria-label="About our app"></section>
<div class="abs section-head" style="top:1340px">
  <h2>ABOUT OUR APP</h2>
  <div class="divider"><span></span></div>
  <p>Lorem ipsum dolor sit amet, consectetur adipisicing elit, sed do eiusmod tempor cot incididunt ut labore<br>Lorem ipsum dolor sit amet, consectetur adipisicing incididunt.</p>
</div>
<div class="abs about-copy">
  <h3>Take a Look Around our App</h3>
  <p>Lorem ipsum dolor sit amet, consectetur adipiscing elit. Aenean commodo ligula eget dolor. Aenean massa. Cum sociis natoque penatibus et magnis dis parturient montes, nascetur ridiculus mus. Donec quam felis, ultricies nec, pellentesque eu. Lorem ipsum dolor sit amet, consectetur adipiscing elit. Aenean commodo ligula eget dolor. Aenean massa. Cum sociis natoque penatibus et magnis dis parturient montes, nascetur ridiculus mus. Donec quam felis, ultricies nec, pellentesque eu</p>
</div>
<div class="abs device about-laptop" role="img" aria-label="Laptop with the app open"></div>

<div class="abs section-head" style="top:1994px">
  <h2>FREQUENTLY ASKED QUESTIONS</h2>
  <div class="divider"><span></span></div>
  <p>Lorem ipsum dolor sit amet, consectetur adipisicing elit, sed do eiusmod tempor cot incididunt ut labore<br>Lorem ipsum dolor sit amet, consectetur adipisicing incididunt.</p>
</div>
<div class="abs timeline"></div>
<div class="abs node" style="top:2180px"></div>
<div class="abs node" style="top:2359px"></div>
<div class="abs node" style="top:2432px"></div>
<div class="abs node" style="top:2506px"></div>
<div class="abs faq-item open" style="top:2166px;height:152px">
  <h4>1. Sedeiusmod tempor inccsetetur aliquatraiy?</h4><span class="toggle"></span>
  <p>Lorem ipsum dolor sit amet, consectetur adipisicing elit, sed do eiusmod tempor incididunt ut labore et dolore magna aliqua. Ut enim ad minim veniam, quis nostrud exercitation ullamco laboris nisi ut aliquip ex ea commodo consequat. Duis aute dolor in reprehenderit in voluptate velit esse cillum dolore</p>
</div>
<div class="abs faq-item" style="top:2345px;height:44px"><h4>2. Lorem ipsum dolor amet, consectetur adipiscing elit?</h4><span class="toggle"></span></div>
<div class="abs faq-item" style="top:2418px;height:44px"><h4>3. Tempor incididunt aliquatraiy?</h4><span class="toggle"></span></div>
<div class="abs faq-item" style="top:2492px;height:44px"><h4>4. Consectetur adipisicing elit, sed do eiusmod tempor?</h4><span class="toggle"></span></div>
<div class="abs faq-phone" role="img" aria-label="Smartphone showing the app's shopper statistics screen"></div>

<section class="abs cta" aria-label="Use our web app today"></section>
<h2 class="abs cta" style="background:none;height:auto;width:auto;left:171px;top:2732px;color:var(--white);font-size:25px;font-weight:700;letter-spacing:.5px">USE OUR WEB APP TODAY</h2>
<p class="abs cta-text">Lorem ipsum dolor sit amet, consectetur adipisicing elit, sed do eiusmod tempor cot incididunt ut labore Lorem ipsum dolor sit amet, consectetur adipisicing incididunt.</p>
<div class="abs btn-ghost">START NOW</div>
<div class="abs cta-phones" role="img" aria-label="Two smartphones showing the app sign-in and dashboard"></div>

<div class="abs map" role="img" aria-label="Map showing the office location"></div>
<div class="abs map-pin"></div>
<div class="abs subscribe">
  <h3>SUBSCRIBE NOW</h3>
  <div class="field">Enter Your Email Address
    <span class="send"><svg width="20" height="18" viewBox="0 0 20 18"><path d="M1 8L19 1 14 17 10 10z" fill="#fff"/></svg></span>
  </div>
</div>

<footer class="abs footer"></footer>
<div class="abs contact-card">
  <h3>Get In Touch</h3>
  <div class="input" style="top:146px">Your name</div>
  <div class="input" style="top:198px">Your email</div>
  <div class="input" style="top:250px">Subject</div>
  <div class="input" style="top:302px;height:52px">Write Message</div>
  <div class="btn-send">SEND MESSAGE</div>
</div>
<div class="abs address-panel">
  <h3>Address</h3>
  <p class="lead">Lorem ipsum dolor sit amet, consectetur adipiscin elit, sed do eiusmod tempor incididunt ut labore et dolore magna aliqua.</p>
  <div class="contact-line" style="top:262px"><span class="ico"><svg width="10" height="10" viewBox="0 0 10 10"><path d="M2 1l2 2-1 1.5a6 6 0 0 0 2.5 2.5L7 6l2 2-1.5 1.5C4 9 1 6 .5 2.5z" fill="#fff"/></svg></span>+0044 545 310 74</div>
  <div class="contact-line" style="top:302px"><span class="ico"><svg width="10" height="8" viewBox="0 0 10 8"><rect x=".5" y=".5" width="9" height="7" fill="none" stroke="#fff"/><path d="M.5 .5L5 4.5 9.5 .5" fill="none" stroke="#fff"/></svg></span>HELLO@VANTRIZO.COM</div>
  <div class="contact-line" style="top:342px"><span class="ico"><svg width="8" height="11" viewBox="0 0 8 11"><path d="M4 11S0 6 0 4a4 4 0 0 1 8 0c0 2-4 7-4 7z" fill="#fff"/></svg></span>14 Marlow Court, Harbour Lane<br>Westbridge, UK</div>
</div>
<div class="abs socials"><span></span><span></span><span></span><span></span></div>
<p class="abs copyright">Copyright © 2017. All right reserved.</p>

</body>
</html>
```